My project benefits Military, First Responders, Police, Fire, and Educators.

Contact Information for Business Card

2 Sided appointment card. Visual side will have my head shot with "Summit Venture" in a bold graffic/text. I am picturing maybe the headshot applied to a filter that has a matrix effect where the picture is made up of data/numbers flowing vertically through the photo. I am of course open to other concepts as well. Side two will have contact info presented in an attractive visual complimenting the front.

```html
<!DOCTYPE html>
<html lang="en">
<head>
<meta charset="utf-8">
<title>Summit Venture – Appointment Card</title>
<link rel="stylesheet" href="https://fonts.googleapis.com/css2?family=Cinzel:wght@400;600&family=Lato:wght@400&family=Arimo:wght@400;700&family=Tinos&display=swap">
<style>
  :root {
    --page: #ffffff;
    --night: #05060c;
    --navy: #141a3c;
    --rain-blue: #1d3f7a;
    --rain-green: #1f5a3a;
    --gold: #ffe6a6;
    --gold-glow: rgba(255, 170, 40, 0.85);
    --white: #ffffff;
    --title-yellow: #f4e33a;
    --panel: rgba(244, 244, 250, 0.94);
    --ink: #111111;
    --rule: #222222;
    --ghost: rgba(255, 255, 255, 0.55);
  }
  * { margin: 0; padding: 0; box-sizing: border-box; }
  html, body { width: 1022px; height: 1200px; overflow: hidden; background: var(--page); }
  .sheet { position: relative; width: 1022px; height: 1200px; }

  .card { position: absolute; left: 0; width: 1022px; overflow: hidden; }
  .card--front { top: 0; height: 600px; }
  .card--back { top: 604px; height: 596px; }

  .data-rain {
    position: absolute; inset: 0;
    background:
      radial-gradient(ellipse at 20% 10%, var(--rain-blue) 0%, transparent 55%),
      radial-gradient(ellipse at 90% 40%, rgba(60, 60, 70, 0.6) 0%, transparent 50%),
      linear-gradient(180deg, var(--navy) 0%, var(--night) 85%);
  }
  .card--back .data-rain {
    background:
      radial-gradient(ellipse at 5% 60%, var(--rain-green) 0%, transparent 35%),
      linear-gradient(180deg, var(--navy) 0%, #0a0d22 100%);
  }

  .portrait {
    position: absolute; left: 68px; top: 0; width: 320px; height: 600px;
    background:
      radial-gradient(ellipse at 55% 35%, #c8506e 0%, #6a3a7a 35%, transparent 60%),
      linear-gradient(180deg, #2a3f78 0%, #1b1f3a 60%, #0c0e1c 100%);
  }

  .brand { position: absolute; left: 480px; top: 118px; width: 520px; text-align: center;
    font-family: "Cinzel", serif; color: var(--gold);
    text-shadow: 0 0 6px var(--gold-glow), 0 0 14px var(--gold-glow); }
  .brand__main { display: block; font-size: 90px; font-weight: 400; line-height: 1; letter-spacing: 2px; }
  .brand__sub { display: block; font-size: 62px; font-weight: 400; line-height: 1; margin-top: 12px; color: #fff3d6; }

  .contact { position: absolute; left: 420px; top: 352px; width: 580px; text-align: center; color: var(--white); }
  .contact__name { font-family: "Arimo", sans-serif; font-weight: 700; font-size: 42px; line-height: 1; }
  .contact__role { font-family: "Arimo", sans-serif; font-size: 21px; color: var(--title-yellow); margin-top: 6px; }
  .contact__line { font-family: "Lato", sans-serif; font-size: 21px; margin-top: 8px; }
  .contact__line span + span { margin-left: 18px; }

  .panel { position: absolute; left: 62px; top: 57px; width: 900px; height: 483px; background: var(--panel); }
  .panel__ghost { position: absolute; left: 0; right: 0; top: 108px; text-align: center;
    font-family: "Cinzel", serif; color: var(--ghost); line-height: 1; }
  .panel__ghost-main { display: block; font-size: 74px; letter-spacing: 2px; }
  .panel__ghost-sub { display: block; font-size: 48px; margin-top: 12px; }

  .form { font-family: "Tinos", serif; color: var(--ink); font-size: 20px; }
  .form__heading { position: absolute; right: 58px; top: 38px; }
  .form__label { position: absolute; left: 56px; }
  .form__rule { position: absolute; height: 2px; background: var(--rule); right: 62px; }
</style>
</head>
<body>
<main class="sheet">

  <section class="card card--front">
    <div class="data-rain" role="img" aria-label="Dark background of vertical streams of glowing data characters"></div>
    <div class="portrait" role="img" aria-label="Headshot of the managing director overlaid with vertical data streams"></div>
    <h1 class="brand">
      <span class="brand__main">SUMMIT</span>
      <span class="brand__sub">VENTURE</span>
    </h1>
    <div class="contact">
      <p class="contact__name">Daniel Reyes</p>
      <p class="contact__role">Managing Director</p>
      <p class="contact__line"><span>P: +00 041 555 218</span><span>E: hello@summitventure.com</span></p>
      <p class="contact__line">118 Harbor Street, Portland 40512</p>
    </div>
  </section>

  <section class="card card--back">
    <div class="data-rain" role="img" aria-label="Dark navy background of vertical streams of data characters"></div>
    <div class="panel form">
      <div class="panel__ghost" aria-hidden="true">
        <span class="panel__ghost-main">SUMMIT</span>
        <span class="panel__ghost-sub">VENTURE</span>
      </div>
      <p class="form__heading">Appointment</p>
      <p class="form__label" style="top:106px">Name</p>
      <div class="form__rule" style="left:128px; top:127px"></div>
      <p class="form__label" style="top:181px">Time</p>
      <div class="form__rule" style="left:128px; top:202px"></div>
      <p class="form__label" style="top:256px">Description</p>
      <div class="form__rule" style="left:186px; top:274px"></div>
      <div class="form__rule" style="left:56px; top:343px"></div>
      <div class="form__rule" style="left:56px; top:413px"></div>
    </div>
  </section>

</main>
</body>
</html>
```